Sudden Tides "Lantern Road" New Single Cover

Create cover artwork for the band Sudden Tides' new single "Lantern Road" being released early 2020. Style, font and graphics to be consistent with band's previous releases and overall brand identity. Visit www.suddentidesband.example and our Spotify page https://music.example.net/artist/7QzWpLx3RtVnKd8e2YbHcJ?si=MUrTgKa4PLe7skvWq2AmZd to view our previous releases and overall brand identity. Some examples attached as well. We are looking for someone to work with on future projects as well.

Lyrics are here: https://docs.example.org/document/d/3KTp9wrn_2ZQa8eXb4Lo_fimH7C5m83Jz4Pd70hrtVcA/edit

Music is here: https://audiostream.example.com/suddentides/lantern-road/s-pzkwa

Font styles to use
Sans Serif

Colors

Designer to choose colors to be used in the design.

Requirements
Must have
• Must be consistent with current brand identity and with prior album / single art.

```html
<!DOCTYPE html>
<html lang="en">
<head>
<meta charset="utf-8">
<title>Sudden Tides – Lantern Road</title>
<link rel="stylesheet" href="https://fonts.googleapis.com/css2?family=Josefin+Sans:wght@400;600&display=swap">
<style>
  :root {
    --teal: #27a8a3;
    --sage: #7fa968;
    --mustard: #c6ad50;
    --amber: #f5a82c;
    --navy: #1d2f5a;
    --white: #ffffff;
  }
  html, body {
    margin: 0;
    padding: 0;
    width: 1200px;
    height: 1200px;
    overflow: hidden;
  }
  .cover {
    position: relative;
    width: 1200px;
    height: 1200px;
    background: linear-gradient(180deg, var(--teal) 0%, var(--sage) 45%, var(--mustard) 70%, var(--amber) 100%);
    font-family: "Josefin Sans", sans-serif;
  }
  .cover__frame {
    position: absolute;
    left: 48px;
    top: 56px;
    width: 1101px;
    height: 1101px;
    border: 2px solid var(--white);
    box-sizing: border-box;
  }
  .cover__title {
    position: absolute;
    left: 0;
    top: 0;
    width: 1200px;
    height: 800px;
  }
  .cover__title text {
    font-family: "Josefin Sans", sans-serif;
    font-weight: 400;
    fill: var(--navy);
  }
  .band-name {
    position: absolute;
    left: 0;
    top: 900px;
    width: 1200px;
    margin: 0;
    text-align: center;
    color: var(--white);
    font-family: "Josefin Sans", sans-serif;
    font-weight: 600;
    font-size: 58px;
    line-height: 66px;
    letter-spacing: 6px;
  }
  .band-name span { display: block; }
</style>
</head>
<body>
<main class="cover">
  <div class="cover__frame"></div>

  <svg class="cover__title" viewBox="0 0 1200 800" aria-labelledby="single-title">
    <title id="single-title">Lantern Road</title>
    <defs>
      <radialGradient id="burst-tone" cx="50%" cy="50%" r="50%">
        <stop offset="0%" stop-color="#9aa85c" stop-opacity="0"/>
        <stop offset="35%" stop-color="#9aa85c" stop-opacity="0"/>
        <stop offset="100%" stop-color="#1d2f5a" stop-opacity="0.35"/>
      </radialGradient>
    </defs>
    <text class="title-line title-line--top" x="140" y="486" font-size="300"
          textLength="940" lengthAdjust="spacingAndGlyphs">LANTERN</text>
    <g class="title-line title-line--bottom" font-size="330">
      <text x="250" y="764" text-anchor="middle">R</text>
      <text x="490" y="764" text-anchor="middle">O</text>
      <text x="745" y="764" text-anchor="middle">A</text>
      <text x="965" y="764" text-anchor="middle">D</text>
    </g>
    <circle class="sunburst" cx="490" cy="640" r="92" fill="url(#burst-tone)"
            role="img" aria-label="Sunburst ornament of fine radiating lines inside the letter O"/>
  </svg>

  <p class="band-name"><span>SUDDEN</span><span>TIDES</span></p>
</main>
</body>
</html>
```